Love pets? Create a veterinary business card that aligns with our new revamped website.

Greetings! We are a five-doctor veterinary hospital that seeks your expertise in designing a new business card that harmonizes with our recently revitalized website: www.tqrn.net. The card should feature our logo, the five doctors, operating hours, contact information, and communicate our purpose and personality.

Contact Information for Business Card

TBA

```html
<!DOCTYPE html>
<html lang="en">
<head>
<meta charset="utf-8">
<title>Maple Hollow Veterinary Hospital – Business Card</title>
<link rel="stylesheet" href="https://fonts.googleapis.com/css2?family=Dancing+Script:wght@600;700&family=Roboto:wght@400;500&family=Roboto+Condensed:wght@400;700&display=swap">
<style>
  :root {
    --stage: #dcdcdc;
    --cream-light: #f3dcab;
    --cream: #ecd3a0;
    --cream-deep: #e2c48c;
    --green: #3e9a2f;
    --gold: #a8741d;
    --brown: #9c6a18;
    --photo-light: #9bb04c;
    --photo-dark: #5d4a36;
  }
  * { box-sizing: border-box; margin: 0; padding: 0; }
  html, body { width: 1200px; height: 846px; overflow: hidden; background: var(--stage); }
  .canvas { position: relative; width: 1200px; height: 846px; }

  .card {
    position: absolute; top: 268px; width: 540px; height: 309px;
    overflow: hidden; box-shadow: 0 10px 24px rgba(0,0,0,.22);
  }
  .card--front { left: 40px; background: linear-gradient(160deg, var(--cream-light), var(--cream) 55%, var(--cream-deep)); }
  .card--back { left: 620px; background: var(--brown); }

  /* front */
  .photo-frame {
    position: absolute; right: -4px; top: -4px; width: 262px; height: 238px;
    border-left: 5px solid var(--green); border-bottom: 5px solid var(--green);
    border-bottom-left-radius: 130px; overflow: hidden;
  }
  .photo-fill {
    width: 100%; height: 100%;
    background: radial-gradient(circle at 55% 55%, var(--photo-dark) 0 30%, transparent 55%),
                linear-gradient(150deg, #c9a33a, var(--photo-light) 40%, #6f8a3a);
  }
  .brand { position: absolute; left: 30px; top: 58px; display: flex; align-items: center; gap: 10px; }
  .brand__dot { width: 30px; height: 30px; border-radius: 50%; background: var(--green); }
  .brand__name { font: 500 24px/1 "Roboto", sans-serif; color: var(--green); }
  .brand__sub { font: 400 9.5px/1 "Roboto", sans-serif; letter-spacing: 1px; color: var(--gold); margin-top: 4px; }

  .person { position: absolute; left: 72px; top: 112px; font: 700 34px/1 "Dancing Script", cursive; color: var(--green); }
  .contact { position: absolute; left: 72px; top: 160px; list-style: none; }
  .contact li { display: flex; align-items: center; gap: 9px; font: 400 15px/21px "Roboto", sans-serif; color: var(--gold); }
  .contact svg { width: 13px; height: 13px; fill: var(--gold); flex: none; }
  .address { position: absolute; left: 94px; top: 252px; font: 400 14.5px/19px "Roboto", sans-serif; color: var(--gold); }

  /* back */
  .grain {
    position: absolute; inset: 0;
    background: linear-gradient(172deg, var(--cream-light) 0 30%, var(--cream) 42%, #c99a4e 56%, var(--brown) 70%);
  }
  .brand--back { left: 60px; top: 96px; }
  .brand--back .brand__dot { background: var(--gold); }
  .brand--back .brand__name { color: var(--gold); }
  .hours-title { position: absolute; left: 180px; top: 160px; font: 700 40px/1 "Dancing Script", cursive; color: var(--cream-light); }
  .hours { position: absolute; left: 70px; top: 222px; display: flex; gap: 34px; }
  .hours__day { font: 700 14px/1.2 "Roboto Condensed", sans-serif; color: var(--cream-light); letter-spacing: .3px; }
  .hours__time { font: 400 14px/1.4 "Roboto Condensed", sans-serif; color: var(--cream-light); }
</style>
</head>
<body>
<div class="canvas">

  <section class="card card--front">
    <div class="photo-frame"><div class="photo-fill" role="img" aria-label="Photo of two cats with their tails forming a heart on a grassy path"></div></div>

    <div class="brand">
      <span class="brand__dot"></span>
      <div>
        <div class="brand__name">Maple Hollow</div>
        <div class="brand__sub">VETERINARY HOSPITAL</div>
      </div>
    </div>

    <div class="person">Name Lastname</div>

    <ul class="contact">
      <li><svg viewBox="0 0 24 24"><path d="M6.6 10.8a15 15 0 0 0 6.6 6.6l2.2-2.2c.3-.3.7-.4 1-.2 1.1.4 2.3.6 3.6.6.6 0 1 .4 1 1V20c0 .6-.4 1-1 1A17 17 0 0 1 3 4c0-.6.4-1 1-1h3.5c.6 0 1 .4 1 1 0 1.3.2 2.5.6 3.6.1.3 0 .7-.2 1z"/></svg>(555) 210-4471</li>
      <li><svg viewBox="0 0 24 24"><path d="M6 2h9v6H6zM4 9h16v13H4zm3 3v2h2v-2zm4 0v2h2v-2zm4 0v2h2v-2zm-8 4v2h2v-2zm4 0v2h2v-2zm4 0v2h2v-2z"/></svg>(555) 208-3390</li>
      <li><svg viewBox="0 0 24 24"><path d="M2 5h20v14H2zm2 2v.5l8 5 8-5V7l-8 5z"/></svg>info@tqrn.net</li>
      <li><svg viewBox="0 0 24 24"><path d="M12 2a10 10 0 1 0 0 20 10 10 0 0 0 0-20zm6.9 6h-3a15 15 0 0 0-1.3-3.9A8 8 0 0 1 18.9 8zM12 4c.8 1.2 1.5 2.5 1.9 4h-3.8c.4-1.5 1.1-2.8 1.9-4zM4.3 14a8 8 0 0 1 0-4h3.4a16 16 0 0 0 0 4zm.8 2h3a15 15 0 0 0 1.3 3.9A8 8 0 0 1 5.1 16zm3-8h-3a8 8 0 0 1 4.3-3.9C8.8 5.3 8.4 6.6 8.1 8zM12 20c-.8-1.2-1.5-2.5-1.9-4h3.8c-.4 1.5-1.1 2.8-1.9 4zm2.3-6H9.7a14 14 0 0 1 0-4h4.6a14 14 0 0 1 0 4zm.3 5.9c.6-1.2 1-2.5 1.3-3.9h3a8 8 0 0 1-4.3 3.9zM16.3 14a16 16 0 0 0 0-4h3.4a8 8 0 0 1 0 4z"/></svg>www.tqrn.net</li>
    </ul>
    <p class="address">4820 Cedar Hill Lane,<br>Brookfield, TX 75010</p>
  </section>

  <section class="card card--back">
    <div class="grain" role="img" aria-label="Decorative wood grain pattern fading from cream to golden brown"></div>

    <div class="brand brand--back">
      <span class="brand__dot"></span>
      <div>
        <div class="brand__name">Maple Hollow</div>
        <div class="brand__sub">VETERINARY HOSPITAL</div>
      </div>
    </div>

    <h2 class="hours-title">Hospital Hours</h2>
    <div class="hours">
      <div><div class="hours__day">MONDAY TO FRIDAY:</div><div class="hours__time">7:00am – 6:00pm</div></div>
      <div><div class="hours__day">SATURDAY:</div><div class="hours__time">8:00am – 12:00pm</div></div>
      <div><div class="hours__day">SUNDAY:</div><div class="hours__time">CLOSED</div></div>
    </div>
  </section>

</div>
</body>
</html>
```